Pale Lantern Double Sided Flyer Design

We need a double sided flyer (1/3 of an A4 which is 99mm x 210mm) developed for our Newcastle(NSW) tour. This flyer will be placed in tourist information centres and hotels. We want it to direct people to our website or be able to make bookings over the phone.

About Us:-
We are a city walking tour company that runs tours day or night. We run both day and night and will incorporate real history / real Pale lantern. Some of the stories will be quite serious i.e.- there are infamous murders from 100 years ago, baffling court cases, even a bit of poetry written by murderers, suicides, love triangles, you name it. We will be telling the historical stories that tourists will not hear from any other tour provider. A bit of darkness, a bit of mystery and a bit of history theme.

We do no go for scares and let the very real stories deliver the entertainment for our guests. Our customers enjoy our tours, but it isn't light fun and frivolity. Our stories are being carefully crafted and are packed with unexpected twists, turns; revelations whilst remaining all 100% true. We deliver deep, rich, engaging stories.

Here are a few samples of quotes from the characters in our stories that may give you an idea of the kind of history we will cover:-

"There were bits of spines, bits of skulls, [and] finger bones spilled out all over the streets - I ended up filling three boxes. Children were playing with them for weeks”

"I had a close shave last night and now I want a close haircut.”

“She's a beautiful child', isn't she? She's the cause of all the trouble.”

“I did it because she would not come home with me.”

"I have killed my wife. I’m glad she’s dead.”

"Stand aside or I'll put a bullet through both of you."

“You villain, I'll teach you to take away my character."

“You’re not dead yet, you bastard!”

Our website, booking form and contact details can be viewed at www.palelantern.com.au

Target Market(s)

Tourists

Industry/Entity Type

Tour

Colors

Designer to choose colors to be used in the design.

Requirements
Must have
• Vertical orientation please.
• Please also include a reference to a discount offer of 25% using the promo code "WICK".
Nice to have
• FRONT FLYER INFORMATION
• - Pale Lantern Logo
• - "I have killed my wife; I'm glad she's dead."
• - Harbourside Hidden Lanes Walk
• - 25% Discount Offer Codeword WICK
• - web address at the base; www.palelantern.com.au
• BACK FLYER INFORMATION
• - "She's a beautiful child', isn't she? She's the cause of all the trouble.
• - Pale Lantern Logo at the base along with the web address www.palelantern.com.au
• - Blurb:- Pale lantern brings back Newcastle's hidden past, the forgotten past, the dark past that may not want to be remembered.
• Real stories from the streets around you. Discover the histories you won't hear anywhere else. The forgotten stories of yesteryear finally get a chance to be told. Through you they get to live again.
Should not have
• GENERAL
• Please do not include the phone number, email address or social media icons. We want to drive online bookings.

```html
<!DOCTYPE html>
<html lang="en">
<head>
<meta charset="utf-8">
<title>Pale Lantern – Harbourside Hidden Lanes Walk</title>
<link rel="stylesheet" href="https://fonts.googleapis.com/css2?family=IM+Fell+English+SC&family=Raleway:wght@500;600&display=swap">
<style>
  :root {
    --ink-white: #f4f2f2;
    --accent-red: #e0475e;
    --mist-light: #8a8a8a;
    --mist-mid: #4a4a4a;
    --night: #141414;
    --band: rgba(20, 20, 20, 0.78);
  }
  html, body {
    margin: 0;
    padding: 0;
    width: 861px;
    height: 1200px;
    overflow: hidden;
    background: var(--night);
  }
  .flyer {
    position: relative;
    width: 861px;
    height: 1200px;
    overflow: hidden;
    color: var(--ink-white);
    text-align: center;
  }
  .forest-backdrop {
    position: absolute;
    inset: 0;
    background:
      radial-gradient(ellipse 70% 40% at 55% 22%, rgba(200,200,200,0.45), rgba(200,200,200,0) 70%),
      linear-gradient(180deg, var(--mist-light) 0%, var(--mist-mid) 35%, #262626 60%, var(--night) 100%);
  }
  .invite-band {
    position: absolute;
    top: 0;
    left: 0;
    right: 0;
    height: 120px;
    background: var(--band);
    display: flex;
    align-items: center;
    justify-content: center;
  }
  .invite-line {
    margin: 0;
    font-family: "Raleway", sans-serif;
    font-weight: 600;
    font-size: 37px;
    letter-spacing: 4.5px;
    text-transform: uppercase;
    white-space: nowrap;
  }
  .tour-title {
    position: absolute;
    top: 147px;
    left: 0;
    right: 0;
    margin: 0;
    font-family: "IM Fell English SC", serif;
    font-weight: 400;
    font-size: 90px;
    line-height: 84px;
    text-transform: uppercase;
    white-space: nowrap;
  }
  .title-line { display: block; }
  .accent { color: var(--accent-red); }
  .discount-offer {
    position: absolute;
    top: 602px;
    left: 0;
    right: 0;
    margin: 0;
    font-family: "IM Fell English SC", serif;
    font-size: 98px;
    line-height: 89px;
    text-transform: uppercase;
    white-space: nowrap;
  }
  .offer-line { display: block; }
  .booking {
    position: absolute;
    top: 1040px;
    left: 0;
    right: 0;
    margin: 0;
    font-family: "Raleway", sans-serif;
    font-weight: 500;
    font-size: 38px;
    line-height: 80px;
    letter-spacing: 5px;
    text-transform: uppercase;
    color: var(--accent-red);
    white-space: nowrap;
  }
  .booking-line { display: block; }
</style>
</head>
<body>
  <main class="flyer">
    <div class="forest-backdrop" role="img" aria-label="Misty dark forest with bare trees fading into fog"></div>

    <header class="invite-band">
      <p class="invite-line">Pale Lantern invites you to a</p>
    </header>

    <h1 class="tour-title">
      <span class="title-line">Harbourside</span>
      <span class="title-line accent">Hidden</span>
      <span class="title-line">Lanes <span class="accent">Walk</span></span>
    </h1>

    <p class="discount-offer">
      <span class="offer-line">25% Discount</span>
      <span class="offer-line">Offer</span>
      <span class="offer-line">Codeword:</span>
      <span class="offer-line">WICK</span>
    </p>

    <p class="booking">
      <span class="booking-line">Book a tour</span>
      <span class="booking-line">at:www.palelantern.com.au</span>
    </p>
  </main>
</body>
</html>
```